Young adult personal development needs podcast 1400x1400 logo

We need artwork done for a podcast logo. The podcast is called The Brightwillers Podcast and is aimed at ages 20-30 waking up and wanting to make changes in their lives.

Using either of the two photos with the logo at bottom right of picture.

Somewhere it says: The Brightwillers Podcast: Educating & inspiring you to reach your greatest potential.

"The Brightwillers Podcast: Educating & inspiring you to reach your greatest potential.

With a strong belief in mentors and role models being a key factor to anyones success, Marcus has placed himself along side the best in their fields.

Diving into movement, primal patterns, mindfulness, creativity and even the influence our gut has over our brain, these experts are going to show you how these pieces paint the picture that is your greatest potential."

Industry/Entity Type

Adult

```html
<!DOCTYPE html>
<html lang="en">
<head>
<meta charset="utf-8">
<title>The Brightwillers Podcast</title>
<link href="https://fonts.googleapis.com/css2?family=Josefin+Sans:wght@400&display=swap" rel="stylesheet">
<style>
  :root {
    --ink: #0f2c5e;
    --sky-top: #2a6bd0;
    --sky-mid: #4d98e6;
    --haze: #d3e8f8;
    --sea: #5b9ccb;
    --sea-deep: #3f7fae;
    --land: #6f9a5c;
    --land-dark: #4b733f;
    --white: #ffffff;
  }
  html, body {
    margin: 0;
    padding: 0;
    width: 1200px;
    height: 1200px;
    overflow: hidden;
    background: var(--sky-top);
  }
  .cover {
    position: relative;
    width: 1200px;
    height: 1200px;
    overflow: hidden;
    font-family: "Josefin Sans", sans-serif;
    color: var(--ink);
  }
  .cover__scene {
    position: absolute;
    inset: 0;
    width: 1200px;
    height: 1200px;
  }
  .title {
    position: absolute;
    left: 0;
    width: 1200px;
    margin: 0;
    text-align: center;
    font-weight: 400;
    line-height: 1;
    text-transform: uppercase;
  }
  .title__the {
    top: 150px;
    font-size: 102px;
    letter-spacing: 4px;
  }
  .title__name {
    top: 254px;
    font-size: 104px;
    letter-spacing: 1px;
  }
  .title__podcast {
    top: 400px;
    font-size: 146px;
    letter-spacing: 48px;
    padding-left: 48px;
    box-sizing: border-box;
  }
  .tagline {
    position: absolute;
    top: 624px;
    left: 0;
    width: 1200px;
    margin: 0;
    text-align: center;
    font-size: 50px;
    line-height: 54px;
    font-variant: small-caps;
    letter-spacing: 1px;
  }
  .website {
    position: absolute;
    left: 46px;
    top: 1118px;
    margin: 0;
    font-size: 31px;
    color: var(--white);
    letter-spacing: 0.5px;
  }
</style>
</head>
<body>
<main class="cover">
  <svg class="cover__scene" viewBox="0 0 1200 1200" role="img" aria-label="Photograph of bright blue sky with soft clouds over the ocean, a man seen from behind on a green hilltop with arms stretched wide">
    <defs>
      <linearGradient id="sky" x1="0" y1="0" x2="0" y2="1">
        <stop offset="0" stop-color="var(--sky-top)"/>
        <stop offset="0.55" stop-color="var(--sky-mid)"/>
        <stop offset="1" stop-color="var(--haze)"/>
      </linearGradient>
      <linearGradient id="sea" x1="0" y1="0" x2="0" y2="1">
        <stop offset="0" stop-color="var(--sea)"/>
        <stop offset="1" stop-color="var(--sea-deep)"/>
      </linearGradient>
      <linearGradient id="land" x1="0" y1="0" x2="0" y2="1">
        <stop offset="0" stop-color="var(--land)"/>
        <stop offset="1" stop-color="var(--land-dark)"/>
      </linearGradient>
    </defs>
    <rect x="0" y="0" width="1200" height="800" fill="url(#sky)"/>
    <rect x="0" y="800" width="1200" height="220" fill="url(#sea)"/>
    <path d="M0 1010 C 250 985, 600 995, 1200 1000 L1200 1200 L0 1200 Z" fill="url(#land)"/>
  </svg>

  <h1 class="title title__the">The</h1>
  <p class="title title__name">Brightwillers</p>
  <p class="title title__podcast">Podcast</p>

  <p class="tagline">Educating &amp; inspiring you<br>to reach your greatest potential.</p>

  <p class="website">brightwillers.com.au</p>
</main>
</body>
</html>
```